Technology Project Portal - Project Listing portal

We require a logo & website designed for our new project.

Project Name: lumrik
Description:
We have a webapp where clients and service providers can come, signup and register development projects. Service providers can the browse projects and contact clients via the portal

Design brief:
Clean & Modern - See Attached color palet & style references. (Feel free to try alternative color palets)

See Project Proposal for site requirements.
UX flow section details pages requires

Examples of all standard UI Components required e.g.
text box / field
Drop down
date picker
etc..
Updates

Target Market(s)

Business / Technology providers

Logo Text

LumRik

Coding

Coded - Design and coding required

Number of Pages Required

5+ page

Requirements
Must have
• Clean Modern Design
Examples for all common UI elements
Templates for common Web App Dialogs e.g. Confirm Delete/Logout etc

```html
<!DOCTYPE html>
<html lang="en">
<head>
<meta charset="UTF-8">
<title>LumRik — Client Dashboard</title>
<link href="https://fonts.googleapis.com/css2?family=Poppins:wght@300;400;500&display=swap" rel="stylesheet">
<style>
  :root{
    --brand:#ff3f0a;
    --ink:#1c1c1c;
    --muted:#b8b8b8;
    --line:#e6e6e6;
    --panel:#f6f6f6;
    --white:#ffffff;
  }
  *{box-sizing:border-box;margin:0;padding:0}
  html,body{width:1200px;height:702px;overflow:hidden;background:var(--white);font-family:'Poppins',sans-serif}
  .dashboard{position:absolute;left:186px;top:28px;width:828px;height:646px;background:var(--white);border:1px solid #ededed;box-shadow:0 6px 18px rgba(0,0,0,.08)}
  .sidebar{position:absolute;left:5px;top:5px;width:66px;height:636px;background:var(--brand);border-radius:26px}
  .sidebar .brand{position:absolute;top:30px;width:100%;text-align:center;color:var(--white);font-size:13px;font-weight:500}
  .nav-item{position:absolute;left:0;width:66px;height:20px;display:flex;justify-content:center;align-items:center}
  .nav-item svg{width:20px;height:20px;fill:none;stroke:var(--white);stroke-width:1.5;stroke-linecap:round;stroke-linejoin:round}
  .nav-item.active{left:11px;width:55px;height:34px;background:var(--white);border-radius:17px 0 0 17px;justify-content:flex-start;padding-left:12px}
  .nav-item.active svg{stroke:var(--brand)}
  .btn-create{position:absolute;left:109px;top:37px;width:118px;height:36px;background:var(--brand);color:var(--white);font-size:9px;font-weight:500;display:flex;align-items:center;justify-content:center}
  .page-title{position:absolute;left:349px;width:200px;top:44px;text-align:center;font-size:16px;font-weight:500;color:var(--ink)}
  .search{position:absolute;left:615px;top:46px;width:122px;height:17px;border-bottom:1px solid var(--line);font-size:8px;color:var(--muted);display:flex;justify-content:space-between;align-items:center;padding:0 2px}
  .search svg{width:8px;height:8px;fill:none;stroke:var(--muted);stroke-width:1.5}
  .avatar{position:absolute;left:750px;top:37px;width:38px;height:38px;border-radius:50%;background:radial-gradient(circle at 50% 40%,#5a4a42,#2b3440)}
  .content{position:absolute;left:109px;top:93px;width:682px;height:517px;background:var(--panel)}
  .card{position:absolute;width:193px;height:211px;background:var(--white)}
  .card .photo{height:135px}
  .card .title{position:absolute;left:10px;top:145px;font-size:12px;color:var(--ink)}
  .card .meta{position:absolute;left:10px;top:164px;font-size:8px;color:var(--muted)}
  .card .views{position:absolute;right:10px;top:149px;font-size:7px;color:var(--muted);display:flex;align-items:center;gap:5px}
  .card .views svg{width:12px;height:8px;fill:none;stroke:var(--muted);stroke-width:1.2}
  .actions{position:absolute;left:0;bottom:0;width:100%;height:28px;border-top:1px solid var(--line);display:flex}
  .action{flex:1;display:flex;align-items:center;justify-content:center;gap:5px;font-size:8px;color:var(--muted)}
  .action+.action{border-left:1px solid var(--line)}
  .action svg{width:12px;height:12px;fill:none;stroke:currentColor;stroke-width:1.1}
  .action.current{color:var(--brand);border-top:1px solid var(--brand);margin-top:-1px}
  .c1{left:37px;top:36px}.c2{left:245px;top:36px}.c3{left:453px;top:36px}
  .c4{left:37px;top:269px}.c5{left:245px;top:269px}.c6{left:453px;top:269px}
  .p1{background:linear-gradient(135deg,#4a4038,#9a8a7a)}
  .p2{background:linear-gradient(135deg,#c9b8a2,#e8e2d8)}
  .p3{background:linear-gradient(135deg,#b0b8bc,#8a5e3e)}
  .p4{background:linear-gradient(135deg,#6e6a58,#a89888)}
  .p5{background:linear-gradient(135deg,#2e3a44,#6a7a8e)}
  .p6{background:linear-gradient(135deg,#e4e4e2,#9a9a96)}
  .corner{position:absolute}
</style>
</head>
<body>
<svg class="corner" style="left:0;top:0" width="80" height="80"><polygon points="0,0 78,0 0,80" fill="var(--brand)"/></svg>
<svg class="corner" style="right:0;bottom:0" width="90" height="90"><polygon points="90,0 90,90 0,90" fill="var(--brand)"/></svg>

<div class="dashboard">
  <aside class="sidebar">
    <div class="brand">lumrik</div>
    <div class="nav-item active" style="top:151px"><svg viewBox="0 0 24 24"><path d="M3 17a9 9 0 0 1 18 0"/><path d="M12 17l4-5"/><path d="M6 13l1 1M12 9v1M18 13l-1 1"/></svg></div>
    <div class="nav-item" style="top:210px"><svg viewBox="0 0 24 24"><rect x="3" y="6" width="18" height="13" rx="1"/><path d="M3 7l9 6 9-6"/></svg></div>
    <div class="nav-item" style="top:257px"><svg viewBox="0 0 24 24"><path d="M6 17V11a6 6 0 0 1 12 0v6l2 2H4z"/><path d="M10 21h4M12 3v2"/></svg></div>
    <div class="nav-item" style="top:305px"><svg viewBox="0 0 24 24"><circle cx="12" cy="12" r="3"/><path d="M12 2l2 3 3-1 1 3 3 1-1 3 2 2-2 2 1 3-3 1-1 3-3-1-2 3-2-3-3 1-1-3-3-1 1-3-2-2 2-2-1-3 3-1 1-3 3 1z"/></svg></div>
    <div class="nav-item" style="top:590px"><svg viewBox="0 0 24 24"><path d="M10 4H5v16h5"/><path d="M10 12h10M16 8l4 4-4 4"/></svg></div>
  </aside>

  <div class="btn-create">Create New Project</div>
  <h1 class="page-title">Client Dashboard</h1>
  <div class="search">Search<svg viewBox="0 0 10 10"><circle cx="4" cy="4" r="3"/><path d="M6.5 6.5L9 9"/></svg></div>
  <div class="avatar" role="img" aria-label="Client profile photo"></div>

  <main class="content">
    <article class="card c1">
      <div class="photo p1" role="img" aria-label="Team working on laptops around a table"></div>
      <div class="title">Project Title</div><div class="meta">48 hrs left</div>
      <div class="views">(301)<svg viewBox="0 0 14 8"><path d="M1 4c3-4 9-4 12 0-3 4-9 4-12 0z"/><circle cx="7" cy="4" r="1.5"/></svg></div>
      <div class="actions"><div class="action current"><svg viewBox="0 0 12 12"><rect x="1.5" y="1" width="9" height="10"/><path d="M3.5 3.5h5M3.5 6h5M3.5 8.5h5"/></svg>Project Details</div><div class="action"><svg viewBox="0 0 12 12"><rect x="1" y="1.5" width="8" height="9.5"/><path d="M6 8l5-5"/></svg>Edit Project</div></div>
    </article>
    <article class="card c2">
      <div class="photo p2" role="img" aria-label="Colleagues shaking hands in a meeting"></div>
      <div class="title">Project Title</div><div class="meta">48 hrs left</div>
      <div class="views">(301)<svg viewBox="0 0 14 8"><path d="M1 4c3-4 9-4 12 0-3 4-9 4-12 0z"/><circle cx="7" cy="4" r="1.5"/></svg></div>
      <div class="actions"><div class="action"><svg viewBox="0 0 12 12"><rect x="1.5" y="1" width="9" height="10"/><path d="M3.5 3.5h5M3.5 6h5M3.5 8.5h5"/></svg>Project Details</div><div class="action"><svg viewBox="0 0 12 12"><rect x="1" y="1.5" width="8" height="9.5"/><path d="M6 8l5-5"/></svg>Edit Project</div></div>
    </article>
    <article class="card c3">
      <div class="photo p3" role="img" aria-label="Overhead view of a team at a wooden table"></div>
      <div class="title">Project Title</div><div class="meta">48 hrs left</div>
      <div class="views">(301)<svg viewBox="0 0 14 8"><path d="M1 4c3-4 9-4 12 0-3 4-9 4-12 0z"/><circle cx="7" cy="4" r="1.5"/></svg></div>
      <div class="actions"><div class="action"><svg viewBox="0 0 12 12"><rect x="1.5" y="1" width="9" height="10"/><path d="M3.5 3.5h5M3.5 6h5M3.5 8.5h5"/></svg>Project Details</div><div class="action"><svg viewBox="0 0 12 12"><rect x="1" y="1.5" width="8" height="9.5"/><path d="M6 8l5-5"/></svg>Edit Project</div></div>
    </article>
    <article class="card c4">
      <div class="photo p4" role="img" aria-label="Team in an office studio"></div>
      <div class="title">Project Title</div><div class="meta">48 hrs left</div>
      <div class="views">(301)<svg viewBox="0 0 14 8"><path d="M1 4c3-4 9-4 12 0-3 4-9 4-12 0z"/><circle cx="7" cy="4" r="1.5"/></svg></div>
      <div class="actions"><div class="action"><svg viewBox="0 0 12 12"><rect x="1.5" y="1" width="9" height="10"/><path d="M3.5 3.5h5M3.5 6h5M3.5 8.5h5"/></svg>Project Details</div><div class="action"><svg viewBox="0 0 12 12"><rect x="1" y="1.5" width="8" height="9.5"/><path d="M6 8l5-5"/></svg>Edit Project</div></div>
    </article>
    <article class="card c5">
      <div class="photo p5" role="img" aria-label="Two colleagues reviewing work on a laptop"></div>
      <div class="title">Project Title</div><div class="meta">48 hrs left</div>
      <div class="views">(301)<svg viewBox="0 0 14 8"><path d="M1 4c3-4 9-4 12 0-3 4-9 4-12 0z"/><circle cx="7" cy="4" r="1.5"/></svg></div>
      <div class="actions"><div class="action"><svg viewBox="0 0 12 12"><rect x="1.5" y="1" width="9" height="10"/><path d="M3.5 3.5h5M3.5 6h5M3.5 8.5h5"/></svg>Project Details</div><div class="action"><svg viewBox="0 0 12 12"><rect x="1" y="1.5" width="8" height="9.5"/><path d="M6 8l5-5"/></svg>Edit Project</div></div>
    </article>
    <article class="card c6">
      <div class="photo p6" role="img" aria-label="Design printouts spread on a desk"></div>
      <div class="title">Project Title</div><div class="meta">48 hrs left</div>
      <div class="views">(301)<svg viewBox="0 0 14 8"><path d="M1 4c3-4 9-4 12 0-3 4-9 4-12 0z"/><circle cx="7" cy="4" r="1.5"/></svg></div>
      <div class="actions"><div class="action"><svg viewBox="0 0 12 12"><rect x="1.5" y="1" width="9" height="10"/><path d="M3.5 3.5h5M3.5 6h5M3.5 8.5h5"/></svg>Project Details</div><div class="action"><svg viewBox="0 0 12 12"><rect x="1" y="1.5" width="8" height="9.5"/><path d="M6 8l5-5"/></svg>Edit Project</div></div>
    </article>
  </main>
</div>
</body>
</html>
```